Post Card for Noel (guarenteed payment)

Hi, We are a language school based in Tunisia and we want to-have a postcard to send to our partners in Germany on the occassion of Christmas. kindly find attached an example of the Christmas card That We want to have. What you can see is the inlay of the card. It's christmas calendar With Some dates and the picture of our team. The card shoulds be foldable horizontal (between the calendar and the text) and the inside shoulds look like the goal of attachment with racing a different background and text, signatures etc. We will need two versions. Digital version of it for email dispatch and one release will be sent via post. The difference is que le That release will be sent via post need a pair of centimeters of blank space entre les text "Das Team von gesamte Valmorix wünscht von Herzen und ein ein friedliches Weihnachtsfest gesundes glückliches und Jahr 2017" and the signatures. We will fill in the blank space with a personal note. Upper portion of the inlay: - Background: Simple in light colors of Valmorix (green / pistachio, white) - 24 calendar windows (see attachment) - 10 windows will be filled with pictures of the staff - Window 24 shoulds contenir the logo of Valmorix - Window 1 shoulds be Tarek - The rest of the windows shoulds be filled Either with numbers or the rest of the pictures Lower share of inlay: - Background: white - On top: Text - Das gesamte Team von Valmorix wünscht von Herzen ein friedliches Weihnachtsfest und ein und gesundes glückliches Jahr 2017! (See attachment for position of the text) - On bottom: Signatures (scanned) and names written out (see attachment) Outside: - Logo Valmorix with corporate background I will add, team pictures asap I Had an idea of Adding a christmas hat to our logo ?? thank you
Industry/Entity Type
School
Look and feel
Each slider illustrates characteristics of the customer's brand and the style your logo design should communicate.

```html
<!DOCTYPE html>
<html lang="de">
<head>
<meta charset="utf-8">
<title>Valmorix – Weihnachtskarte 2016</title>
<link rel="stylesheet" href="https://fonts.googleapis.com/css2?family=Arimo:wght@400;700&family=Josefin+Sans:wght@300;400&display=swap">
<style>
  :root {
    --green-light: #a6bc7e;
    --green-mid: #87a262;
    --green-dark: #668a45;
    --window: #ffffff;
    --window-edge: #7d9658;
    --number: #454545;
    --text: #111111;
    --name: #5a5a5a;
    --ink-wash: #e9e9e9;
    --photo-a: #c9b8a8;
    --photo-b: #b7a495;
    --brand-mark: #d4dc1c;
    --brand-text: #1a1a1a;
  }
  * { margin: 0; padding: 0; box-sizing: border-box; }
  html, body { width: 1200px; height: 1200px; overflow: hidden; background: #fff; }
  .card { position: relative; width: 1200px; height: 1200px; background: #fff; }

  .calendar {
    position: absolute; left: 0; top: 0; width: 1200px; height: 602px;
    background: radial-gradient(ellipse 60% 70% at 50% 45%, var(--green-light) 0%, var(--green-mid) 55%, var(--green-dark) 100%);
  }
  .window {
    position: absolute; width: 100px; height: 100px;
    background: var(--window);
    border: 2px solid var(--window-edge);
    box-shadow: 0 1px 3px rgba(0,0,0,.25);
    display: flex; align-items: center; justify-content: center;
    font-family: "Josefin Sans", sans-serif; font-weight: 300;
    font-size: 58px; color: var(--number); line-height: 1;
    padding-top: 8px;
  }
  .window.wide { width: 228px; }
  .window.tall { height: 228px; }
  .window.photo {
    background: linear-gradient(160deg, var(--photo-a), var(--photo-b));
    border-color: #9aa98a;
  }
  .window.logo { width: 228px; height: 228px; padding: 0; gap: 10px; }
  .logo-dot { width: 22px; height: 22px; border-radius: 50%; background: var(--brand-mark); }
  .logo-name {
    font-family: "Arimo", sans-serif; font-weight: 700; font-size: 34px;
    color: var(--brand-text); letter-spacing: -0.5px;
  }

  .greeting {
    position: absolute; left: 105px; top: 662px; width: 1000px;
    font-family: "Arimo", sans-serif; font-size: 26px; line-height: 34px; color: var(--text);
  }

  .signer { position: absolute; width: 200px; }
  .signature { width: 110px; height: 52px; background: var(--ink-wash); border-radius: 4px; margin-left: 14px; }
  .signer-name {
    margin-top: 10px; font-family: "Arimo", sans-serif; font-size: 21px;
    color: var(--name); white-space: nowrap;
  }
</style>
</head>
<body>
<div class="card">
  <section class="calendar">
    <!-- row 1 -->
    <div class="window photo" style="left:101px;top:70px" role="img" aria-label="Teamfoto: Tarek Haddad"></div>
    <div class="window" style="left:229px;top:70px">4</div>
    <div class="window photo" style="left:357px;top:70px" role="img" aria-label="Teamfoto einer Mitarbeiterin"></div>
    <div class="window" style="left:485px;top:70px">11</div>
    <div class="window photo" style="left:613px;top:70px" role="img" aria-label="Teamfoto einer Mitarbeiterin"></div>
    <div class="window wide" style="left:742px;top:70px">13</div>
    <div class="window photo" style="left:998px;top:70px" role="img" aria-label="Teamfoto einer Mitarbeiterin"></div>
    <!-- row 2 -->
    <div class="window tall" style="left:101px;top:198px">2</div>
    <div class="window photo" style="left:229px;top:198px" role="img" aria-label="Teamfoto einer Mitarbeiterin"></div>
    <div class="window" style="left:357px;top:198px">9</div>
    <div class="window logo" style="left:485px;top:198px">
      <span class="logo-dot"></span><span class="logo-name">Valmorix</span>
    </div>
    <div class="window" style="left:742px;top:198px">20</div>
    <div class="window photo" style="left:870px;top:198px" role="img" aria-label="Teamfoto einer Mitarbeiterin"></div>
    <div class="window" style="left:998px;top:198px">15</div>
    <!-- row 3 -->
    <div class="window wide" style="left:229px;top:326px">6</div>
    <div class="window photo" style="left:742px;top:326px" role="img" aria-label="Teamfoto eines Mitarbeiters"></div>
    <div class="window tall" style="left:870px;top:326px">18</div>
    <div class="window photo" style="left:998px;top:326px" role="img" aria-label="Teamfoto einer Mitarbeiterin"></div>
    <!-- row 4 -->
    <div class="window photo" style="left:101px;top:454px" role="img" aria-label="Teamfoto eines Mitarbeiters"></div>
    <div class="window" style="left:229px;top:454px">7</div>
    <div class="window" style="left:357px;top:454px">8</div>
    <div class="window photo" style="left:485px;top:454px" role="img" aria-label="Teamfoto eines Mitarbeiters"></div>
    <div class="window wide" style="left:613px;top:454px">22</div>
    <div class="window photo" style="left:998px;top:454px" role="img" aria-label="Teamfoto einer Mitarbeiterin"></div>
  </section>

  <p class="greeting">Das gesamte Team von Valmorix wünscht von Herzen ein friedliches Weihnachtsfest und ein gesundes und glückliches Jahr 2017!</p>

  <div class="signer" style="left:97px;top:790px"><div class="signature" role="img" aria-label="Unterschrift Tarek Haddad"></div><div class="signer-name">Tarek Haddad</div></div>

  <div class="signer" style="left:97px;top:910px"><div class="signature" role="img" aria-label="Unterschrift Leila Karoui"></div><div class="signer-name">Leila Karoui</div></div>
  <div class="signer" style="left:328px;top:910px"><div class="signature" role="img" aria-label="Unterschrift Nour Gharbi"></div><div class="signer-name">Nour Gharbi</div></div>
  <div class="signer" style="left:502px;top:910px"><div class="signature" role="img" aria-label="Unterschrift Yassine Ferchichi"></div><div class="signer-name">Yassine Ferchichi</div></div>
  <div class="signer" style="left:702px;top:910px"><div class="signature" role="img" aria-label="Unterschrift Karim Belhadj"></div><div class="signer-name">Karim Belhadj</div></div>
  <div class="signer" style="left:906px;top:910px"><div class="signature" role="img" aria-label="Unterschrift Hatem Ben Salah"></div><div class="signer-name">Hatem Ben Salah</div></div>

  <div class="signer" style="left:97px;top:1020px"><div class="signature" role="img" aria-label="Unterschrift Rania Lea Mejri"></div><div class="signer-name">Rania Lea Mejri</div></div>
  <div class="signer" style="left:328px;top:1020px"><div class="signature" role="img" aria-label="Unterschrift Sonia Bouaziz"></div><div class="signer-name">Sonia Bouaziz</div></div>
  <div class="signer" style="left:502px;top:1020px"><div class="signature" role="img" aria-label="Unterschrift Ines Jebali"></div><div class="signer-name">Ines Jebali</div></div>
  <div class="signer" style="left:702px;top:1020px"><div class="signature" role="img" aria-label="Unterschrift Amel Trabelsi"></div><div class="signer-name">Amel Trabelsi</div></div>
  <div class="signer" style="left:906px;top:1020px"><div class="signature" role="img" aria-label="Unterschrift Walid El Amri"></div><div class="signer-name">Walid El Amri</div></div>
</div>
</body>
</html>
```